International Film making Business needs the 5 Logos provided made into a POSTER Format

Design Task:
CREATE A POSTER DESIGN USING THE 5 LOGOS PROVIDED. The GLAD SKY VISTA LOGO should stand out from the others by being in the middle with the other 4 logos connected to it somehow.

The 5 Businesses already has their 5 Logos, all similar in design to each other.

GLAD SKY VISTA is the Main Logo that encompasses the other 4 Logos. So it must stand out more and it is like the Overall Business entity that incorporates the other 4 Logos.

What is required is that by using the 5 Logo designs provided, create a cool graphic artwork that somehow incorporates ALL of the 5 Logos - But having the GLAD SKY VISTA Logo at the forefront/most important/standing out the most.
- GLAD SKY VISTA will probably be bigger than the others
- and could be changed into 3D.

I have attached all 5 logos and a hand drawn example of how the GLAD SKY VISTAS could stand out from the rest.

THE DESIGNS OF THE LOGOS SHOULD NOT BE CHANGED (except the GLADSKYVISTA which can be 3D)

Please do not be restricted with the sample idea. Creativity is encouraged

DIMENSION: 3000 mm x 6000 mm
high resolution graphic

Logo Text

glad sky , glad sky reels, glad sky tales, glad sky groovy, GLAD SKY VISTAS

Requirements
Must have
• USE THE 5 LOGOS PROVIDED ONLY - Only GLAD SKY VISTA can be changed into 3D only
Nice to have
• Eye catching design, showing the Glad Sky Vista as the most powerful Logo that has the other 4 as subordinate companies
Should not have
• ANY CHANGE IN THE 5 LOGO DESIGNS (EXcept 3D for Glad Sky Vistas)

```html
<!DOCTYPE html>
<html lang="en">
<head>
<meta charset="utf-8">
<title>Glad Sky Vistas – Family of Brands Poster</title>
<link rel="stylesheet" href="https://fonts.googleapis.com/css2?family=Cinzel:wght@400;600&family=Montserrat:wght@400&display=swap">
<style>
  :root {
    --page-bg: #d6d5d6;
    --poster-bg: #1b1b1b;
    --gold-line: #c7a54a;
    --gold-text: #c9a13c;
    --pale-gold: #efe1a0;
    --core-dark: #3f3d3e;
    --white: #ffffff;
    --brand-blue: #4f82c2;
    --brand-red: #d8230f;
    --brand-charcoal: #2e2e2e;
    --brand-green: #5aa02c;
    --tales-purple: #6a3d9a;
    --url-grey: #9a9a9a;
  }
  html, body {
    margin: 0;
    padding: 0;
    overflow: hidden;
  }
  body {
    width: 1130px;
    height: 1200px;
    background: var(--page-bg);
    position: relative;
  }
  .poster {
    position: absolute;
    left: 285px;
    top: 40px;
    width: 560px;
    height: 1120px;
    background: var(--poster-bg);
    box-shadow: 0 6px 18px rgba(0, 0, 0, 0.35);
  }
  .brand-map {
    display: block;
    width: 560px;
    height: 1120px;
  }
  .brand-name {
    font-family: "Cinzel", serif;
    font-weight: 600;
    letter-spacing: 1.5px;
    text-anchor: middle;
  }
  .brand-name--main {
    font-weight: 400;
    letter-spacing: 4px;
  }
  .brand-url {
    font-family: "Montserrat", sans-serif;
    font-size: 8.5px;
    letter-spacing: 1.2px;
    fill: var(--url-grey);
    text-anchor: middle;
  }
</style>
</head>
<body>
  <main class="poster">
    <svg class="brand-map" viewBox="0 0 560 1120" xmlns="http://www.w3.org/2000/svg">
      <!-- connectors from sub-brands to the main brand -->
      <g class="connectors" stroke="var(--gold-line)" stroke-width="1.2">
        <line x1="170" y1="408" x2="182" y2="420"/>
        <line x1="395" y1="408" x2="383" y2="420"/>
        <line x1="170" y1="725" x2="182" y2="713"/>
        <line x1="395" y1="725" x2="383" y2="713"/>
      </g>
      <g class="connector-dots">
        <circle cx="170" cy="408" r="2.5" fill="#cfcfcf"/>
        <circle cx="182" cy="420" r="2.5" fill="var(--brand-blue)"/>
        <circle cx="395" cy="408" r="2.5" fill="#cfcfcf"/>
        <circle cx="383" cy="420" r="2.5" fill="var(--brand-red)"/>
        <circle cx="170" cy="725" r="2.5" fill="#cfcfcf"/>
        <circle cx="182" cy="713" r="2.5" fill="#555"/>
        <circle cx="395" cy="725" r="2.5" fill="#cfcfcf"/>
        <circle cx="383" cy="713" r="2.5" fill="var(--brand-green)"/>
      </g>

      <!-- main brand -->
      <g class="main-brand">
        <circle cx="282" cy="565" r="178" fill="none" stroke="var(--gold-line)" stroke-width="2"/>
        <circle cx="282" cy="565" r="157" fill="var(--pale-gold)"/>
        <circle cx="282" cy="565" r="127" fill="var(--core-dark)"/>
        <text class="brand-name brand-name--main" x="282" y="555" font-size="24" fill="var(--gold-text)">GLAD SKY</text>
        <text class="brand-name brand-name--main" x="282" y="583" font-size="24" fill="var(--gold-text)">VISTAS</text>
        <text class="brand-url" x="282" y="601">gladskyvistas.com.au</text>
      </g>

      <!-- sub-brand: glad sky -->
      <g class="sub-brand sub-brand--core">
        <circle cx="126" cy="344" r="78" fill="none" stroke="var(--gold-line)" stroke-width="1.5"/>
        <circle cx="126" cy="344" r="68" fill="var(--brand-blue)"/>
        <circle cx="126" cy="344" r="60" fill="var(--white)"/>
        <text class="brand-name" x="126" y="350" font-size="16" fill="var(--brand-blue)">GLAD SKY</text>
      </g>

      <!-- sub-brand: glad sky tales -->
      <g class="sub-brand sub-brand--tales">
        <circle cx="439" cy="344" r="78" fill="none" stroke="var(--gold-line)" stroke-width="1.5"/>
        <circle cx="439" cy="344" r="68" fill="var(--brand-red)"/>
        <circle cx="439" cy="344" r="60" fill="var(--white)"/>
        <text class="brand-name" x="439" y="340" font-size="13" fill="var(--tales-purple)">GLAD SKY</text>
        <text class="brand-name" x="439" y="357" font-size="13" fill="var(--tales-purple)">TALES</text>
      </g>

      <!-- sub-brand: glad sky reels -->
      <g class="sub-brand sub-brand--reels">
        <circle cx="126" cy="789" r="78" fill="none" stroke="var(--gold-line)" stroke-width="1.5"/>
        <circle cx="126" cy="789" r="68" fill="var(--brand-charcoal)"/>
        <circle cx="126" cy="789" r="60" fill="var(--white)"/>
        <text class="brand-name" x="126" y="785" font-size="13" fill="var(--brand-charcoal)">GLAD SKY</text>
        <text class="brand-name" x="126" y="802" font-size="13" fill="var(--brand-charcoal)">REELS</text>
      </g>

      <!-- sub-brand: glad sky groovy -->
      <g class="sub-brand sub-brand--groovy">
        <circle cx="439" cy="789" r="78" fill="none" stroke="var(--gold-line)" stroke-width="1.5"/>
        <circle cx="439" cy="789" r="68" fill="var(--brand-green)"/>
        <circle cx="439" cy="789" r="60" fill="var(--white)"/>
        <text class="brand-name" x="439" y="785" font-size="13" fill="var(--brand-green)">GLAD SKY</text>
        <text class="brand-name" x="439" y="804" font-size="15" fill="var(--brand-green)">GROOVY</text>
      </g>
    </svg>
  </main>
</body>
</html>
```